Application Dashboard Skin - Non coded theme only

We are looking for a website color theme/look feel for a new .net dashboard application we are building. Target audience who will be using this are E and C level professionals. We are looking for the following:

Images of optional color themes for our existing dashboard. You can access a temporary version with no styling here: http://vantorquel.net:99/ . Application built in telerik and highcharts.

We are not looking for finished code or application skins. Our development team will take your final design (with specific colors/images/etc. provided) and apply it to the final beta version of the application.

Design considerations:
We are open to creative ideas, but please know that preference will be given to professional designs with emphasis on a consistent brand look/feel. Designs and colors should be focused on quickly identifying and processing the data.

Multiple submissions welcome.

-Pellowrin team

Target Market(s)

IT / Insurance

Industry/Entity Type

Building

Number of Pages Required

3 page

Requirements
Must have
• Application Dashboard link for design: http://vantorquel.net:99/

```html
<!DOCTYPE html>
<html lang="en">
<head>
<meta charset="utf-8">
<title>claimscope – Performance Insight</title>
<link href="https://fonts.googleapis.com/css2?family=Fira+Sans:wght@300;400;500;600&display=swap" rel="stylesheet">
<style>
:root{
  --ink:#353944;
  --orange:#f7941d;
  --bar:#bdbdbd;
  --text:#2f3238;
  --muted:#6b6e75;
  --panel:#f2f3f4;
  --line:#e3e4e6;
  --white:#ffffff;
}
*{box-sizing:border-box;margin:0;padding:0}
html,body{width:873px;height:1200px;overflow:hidden}
body{position:relative;background:var(--white);font-family:"Fira Sans",sans-serif;color:var(--text)}
.topbar{position:absolute;left:0;top:0;width:873px;height:76px;background:var(--ink);border-bottom:1px solid #22252c}
.brand{position:absolute;left:13px;top:22px;color:var(--white)}
.brand-name{font-size:23px;font-weight:500;letter-spacing:-.3px;display:flex;align-items:center;gap:6px}
.brand-dot{width:16px;height:16px;border-radius:50%;background:var(--orange);display:inline-block}
.brand-tag{font-size:8px;font-weight:300;position:absolute;left:128px;top:25px;white-space:nowrap}
.nav{position:absolute;top:33px;left:0;list-style:none}
.nav li{position:absolute;color:var(--white);font-size:9px;font-weight:500;white-space:nowrap}
.main{position:absolute;left:0;top:76px;width:567px;height:1096px;background:var(--white)}
.side{position:absolute;left:567px;top:76px;width:306px;height:1096px;background:var(--panel)}
.section-head{position:absolute;left:0;width:567px;height:34px;border-bottom:1px solid var(--line);font-size:10.5px;font-weight:500;padding:10px 0 0 13px}
.select{position:absolute;height:19px;border:1px solid #d5d6d8;border-radius:2px;background:var(--white);font-size:7.5px;color:#8a8c91;padding:5px 0 0 7px}
.side-head{position:absolute;left:567px;top:77px;width:306px;height:33px;background:var(--white);border-bottom:1px solid var(--line);font-size:10.5px;font-weight:500;padding:9px 0 0 14px}
.tabs{position:absolute;left:0;top:492px;width:567px;height:26px;background:var(--orange);display:flex;padding-left:13px}
.tab{font-size:9px;color:var(--white);font-weight:500;padding:8px 0 0;margin-right:27px}
.tab.active{background:var(--white);color:var(--text);padding:8px 10px 0;margin-right:14px}
.kpi-title{position:absolute;left:567px;top:129px;width:306px;text-align:center;font-size:10px;font-weight:500}
.kpi-sub{position:absolute;left:567px;top:145px;width:306px;text-align:center;font-size:8px;color:var(--muted)}
.kpi-list{position:absolute;left:580px;top:0;list-style:none}
.kpi-list li{position:absolute;left:0;width:285px;font-size:8.8px;color:#4a4d54;display:flex;align-items:center;white-space:nowrap}
.kpi-icon{width:9px;height:9px;border-radius:50%;background:var(--orange);color:var(--white);font-size:6.5px;font-weight:600;text-align:center;line-height:9px;margin-right:9px}
.kpi-val{position:absolute;left:227px;font-size:7px;color:#4a4d54}
.pie-panel{position:absolute;left:567px;width:306px;background:var(--panel)}
.menu-btn{position:absolute;width:27px;height:24px;background:#e6e7e9;border-radius:2px}
.menu-btn i{position:absolute;left:8px;width:11px;height:1px;background:#777}
.footer{position:absolute;left:0;top:1172px;width:873px;height:28px;background:#f0f1f2;font-size:8.8px;color:#6b6e75;padding:7px 0 0 19px}
.charts{position:absolute;left:0;top:0;width:873px;height:1200px;pointer-events:none}
</style>
</head>
<body>

<header class="topbar">
  <div class="brand">
    <div class="brand-name">claimscope <span class="brand-dot"></span></div>
    <div class="brand-tag">Performance Insight</div>
  </div>
  <ul class="nav">
    <li style="left:273px">ACCURACY RESULTS</li>
    <li style="left:386px">PROCESSOR ACCURACY</li>
    <li style="left:514px">MANAGE USERS</li>
    <li style="left:611px">SETTINGS</li>
  </ul>
</header>

<main class="main"></main>
<aside class="side"></aside>

<div class="section-head" style="top:77px">ACCURACY RESULTS</div>
<div class="select" style="left:491px;top:84px;width:63px">End to End ▾</div>

<div class="section-head" style="top:458px;border-top:1px solid var(--line)">ERROR IMPACT FOR JUNE 2016</div>
<div class="select" style="left:491px;top:466px;width:62px">All Regions ▾</div>

<nav class="tabs">
  <div class="tab active">All Errors</div>
  <div class="tab">Providers</div>
  <div class="tab">Employers</div>
  <div class="tab">Line Of Business</div>
</nav>

<div class="side-head">KPI'S</div>
<div class="select" style="left:797px;top:84px;width:63px">All Regions ▾</div>

<div class="kpi-title">Overall YTD Accuracy</div>
<div class="kpi-sub">97.41%</div>
<ul class="kpi-list">
  <li style="top:175px"><span class="kpi-icon">i</span>Claims Audited<span class="kpi-val">4859</span></li>
  <li style="top:199px"><span class="kpi-icon">i</span>Avg. Claims Audited per day<span class="kpi-val">6.7</span></li>
  <li style="top:224px"><span class="kpi-icon">i</span>Errors Found<span class="kpi-val">2147</span></li>
  <li style="top:247px"><span class="kpi-icon">i</span>Financial Impact<span class="kpi-val">$1,462,139</span></li>
  <li style="top:272px"><span class="kpi-icon">i</span>Total Claims Posted<span class="kpi-val">17,773,591</span></li>
  <li style="top:296px"><span class="kpi-icon">i</span>Total Encounter Claims<span class="kpi-val">93,984,586</span></li>
  <li style="top:320px"><span class="kpi-icon">i</span>Total Auto Adjudication Claim Count<span class="kpi-val">920,918</span></li>
  <li style="top:344px"><span class="kpi-icon">i</span>Total Adjustment Claim Count<span class="kpi-val">920,918</span></li>
  <li style="top:369px"><span class="kpi-icon">i</span>Total Denied Claim Count<span class="kpi-val">133,523</span></li>
  <li style="top:393px"><span class="kpi-icon">i</span>Total Dollars Paid<span class="kpi-val">$5,669,835,044</span></li>
  <li style="top:416px"><span class="kpi-icon">i</span>Auto Adjudication Rate<span class="kpi-val">$0.052</span></li>
  <li style="top:441px"><span class="kpi-icon">i</span>Adjustment Rate<span class="kpi-val">1.345%</span></li>
  <li style="top:466px"><span class="kpi-icon">i</span>Denial Rate<span class="kpi-val">0.751%</span></li>
</ul>

<div class="pie-panel" style="top:500px;height:335px;border-top:3px solid var(--white)"></div>
<div class="pie-panel" style="top:837px;height:335px;border-top:3px solid var(--white)"></div>

<div class="menu-btn" style="left:527px;top:134px"><i style="top:8px"></i><i style="top:11px"></i><i style="top:14px"></i></div>
<div class="menu-btn" style="left:235px;top:541px"><i style="top:8px"></i><i style="top:11px"></i><i style="top:14px"></i></div>
<div class="menu-btn" style="left:527px;top:541px"><i style="top:8px"></i><i style="top:11px"></i><i style="top:14px"></i></div>
<div class="menu-btn" style="left:833px;top:520px;background:#fff"><i style="top:8px"></i><i style="top:11px"></i><i style="top:14px"></i></div>
<div class="menu-btn" style="left:833px;top:857px;background:#fff"><i style="top:8px"></i><i style="top:11px"></i><i style="top:14px"></i></div>

<svg class="charts" viewBox="0 0 873 1200" font-family="Fira Sans, sans-serif">
  <!-- YTD accuracy -->
  <g class="chart-accuracy">
    <text x="277" y="139" text-anchor="middle" font-size="10" font-weight="500" fill="#2f3238">YTD Overall Accuracy</text>
    <text x="277" y="154" text-anchor="middle" font-size="8.5" fill="#555">Click the bars to view YTD details for the specific region</text>
    <g stroke="#e6e6e6" stroke-width="1">
      <line x1="60" y1="175" x2="554" y2="175"/><line x1="60" y1="215" x2="554" y2="215"/>
      <line x1="60" y1="256" x2="554" y2="256"/><line x1="60" y1="296" x2="554" y2="296"/>
      <line x1="60" y1="336" x2="554" y2="336"/><line x1="60" y1="377" x2="554" y2="377" stroke="#ccd"/>
    </g>
    <g font-size="7.5" fill="#555" text-anchor="end">
      <text x="47" y="178">100</text><text x="47" y="218">97.5</text><text x="47" y="259">95</text>
      <text x="47" y="299">92.5</text><text x="47" y="339">90</text><text x="47" y="380">87.5</text>
    </g>
    <text transform="translate(19,284) rotate(-90)" font-size="7.5" fill="#888" text-anchor="middle">Overall Accuracy</text>
    <g fill="var(--bar)">
      <rect x="79" y="212" width="47" height="165"/>
      <rect x="174" y="192" width="46" height="185"/>
      <rect x="267" y="230" width="47" height="147"/>
      <rect x="361" y="212" width="47" height="165"/>
      <rect x="455" y="259" width="47" height="118"/>
    </g>
    <g font-size="7" fill="#333" text-anchor="middle">
      <text x="102" y="207">97.7%</text><text x="197" y="187">98.5%</text><text x="290" y="226">96.8%</text>
      <text x="385" y="207">97.7%</text><text x="478" y="253">94.9%</text>
    </g>
    <g font-size="7.8" fill="#333" text-anchor="middle">
      <text x="102" y="395">Colorado</text><text x="197" y="395">Georgia</text><text x="290" y="395">Hawaii</text>
      <text x="385" y="395">MidAtlantic</text><text x="478" y="395">NorthWest</text>
    </g>
  </g>

  <!-- Top 10 error reasons (count) -->
  <g class="chart-errors">
    <text x="122" y="548" text-anchor="middle" font-size="10" font-weight="500" fill="#2f3238">Top 10 Error Reasons</text>
    <text x="122" y="564" text-anchor="middle" font-size="8.5" fill="#555">All Regions</text>
    <g stroke="#eee"><line x1="148" y1="588" x2="148" y2="805"/><line x1="174" y1="588" x2="174" y2="805"/><line x1="202" y1="588" x2="202" y2="805"/><line x1="230" y1="588" x2="230" y2="805"/><line x1="257" y1="588" x2="257" y2="805"/></g>
    <g font-size="7.5" fill="#444" text-anchor="end">
      <text x="134" y="601">Incorrect Contra...</text><text x="134" y="623">Claim Paid Incorre...</text>
      <text x="134" y="645">Not A Norvel Benefit. B...</text><text x="134" y="667">Incorrect Co-Pay ...</text>
      <text x="134" y="689">Copay Amount Not C...</text><text x="134" y="711">Did Not Follow Des...</text>
      <text x="134" y="734">Did Not Follow Pnp</text><text x="134" y="756">Claim Denied In Err...</text>
      <text x="134" y="778">Unknown</text><text x="134" y="800">Denied Incorrectl...</text>
    </g>
    <g fill="var(--bar)">
      <rect x="148" y="594" width="95" height="7"/><rect x="148" y="616" width="71" height="7"/>
      <rect x="148" y="638" width="66" height="7"/><rect x="148" y="660" width="63" height="7"/>
      <rect x="148" y="682" width="55" height="7"/><rect x="148" y="705" width="55" height="7"/>
      <rect x="148" y="727" width="52" height="7"/><rect x="148" y="749" width="38" height="7"/>
      <rect x="148" y="771" width="38" height="7"/><rect x="148" y="793" width="33" height="7"/>
    </g>
    <g font-size="7" fill="#333">
      <text x="252" y="601">35</text><text x="223" y="623">26</text><text x="218" y="645">24</text>
      <text x="215" y="667">23</text><text x="207" y="689">20</text><text x="207" y="711">20</text>
      <text x="204" y="734">19</text><text x="190" y="756">14</text><text x="190" y="778">14</text><text x="185" y="800">12</text>
    </g>
    <g font-size="7" fill="#555" text-anchor="middle">
      <text x="148" y="822">0</text><text x="174" y="822">10</text><text x="202" y="822">20</text>
      <text x="230" y="822">30</text><text x="257" y="822">40</text>
    </g>
    <text x="205" y="846" text-anchor="middle" font-size="7.5" fill="#333">Count</text>
    <text transform="translate(19,703) rotate(-90)" font-size="7.5" fill="#888" text-anchor="middle">All Errors</text>
  </g>

  <!-- Top 10 error reasons (financial impact) -->
  <g class="chart-impact">
    <text x="415" y="548" text-anchor="middle" font-size="10" font-weight="500" fill="#2f3238">Top 10 Error Reasons - Financial Impact</text>
    <text x="415" y="564" text-anchor="middle" font-size="8.5" fill="#555">All Regions</text>
    <g stroke="#eee"><line x1="437" y1="588" x2="437" y2="805"/><line x1="462" y1="588" x2="462" y2="805"/><line x1="491" y1="588" x2="491" y2="805"/><line x1="521" y1="588" x2="521" y2="805"/><line x1="547" y1="588" x2="547" y2="805"/></g>
    <g font-size="7.5" fill="#444" text-anchor="end">
      <text x="426" y="601">Incorrect Contra...</text><text x="426" y="623">Claim Paid Incorre...</text>
      <text x="426" y="645">Not A Norvel Benefit. B...</text><text x="426" y="667">Incorrect Co-Pay ...</text>
      <text x="426" y="689">Copay Amount Not C...</text><text x="426" y="711">Did Not Follow Des...</text>
      <text x="426" y="734">Did Not Follow Pnp</text><text x="426" y="756">Claim Denied In Err...</text>
      <text x="426" y="778">Unknown</text><text x="426" y="800">Denied Incorrectl...</text>
    </g>
    <g fill="var(--orange)">
      <rect x="450" y="593" width="50" height="9"/><rect x="502" y="593" width="39" height="9"/>
      <rect x="498" y="615" width="42" height="9"/>
      <rect x="522" y="659" width="3" height="9"/>
      <rect x="493" y="726" width="48" height="9"/>
      <rect x="526" y="748" width="9" height="9"/>
      <rect x="526" y="792" width="2" height="9"/>
    </g>
    <g font-size="7" fill="#333">
      <text x="451" y="601">$ -65155.67</text><text x="504" y="601">$ 12510.63</text>
      <text x="455" y="623">$ -26915.92</text><text x="501" y="623">$ -2919.39</text>
      <text x="501" y="645">$ -245</text><text x="530" y="645">$0</text>
      <text x="483" y="667">$ -3898.21</text><text x="527" y="667">$ 693.01</text>
      <text x="504" y="689">$-295</text><text x="530" y="689">$ 10</text>
      <text x="513" y="711">$ 0</text><text x="530" y="711">$ 0</text>
      <text x="450" y="734">$ -29341.33</text><text x="501" y="734">$ 10390.26</text>
      <text x="510" y="756">$ 0</text>
      <text x="510" y="778">$ 0</text><text x="530" y="778">$ 331.1</text>
      <text x="499" y="800">$ -1.81</text>
    </g>
    <g font-size="7" fill="#555" text-anchor="middle">
      <text x="437" y="822">-75k</text><text x="462" y="822">-50k</text><text x="491" y="822">-25k</text>
      <text x="521" y="822">0k</text><text x="547" y="822">25k</text>
    </g>
    <text x="496" y="846" text-anchor="middle" font-size="7.5" fill="#333">$ Amount</text>
  </g>

  <!-- Paid vs Denied -->
  <g class="chart-pie-denied">
    <text x="720" y="536" text-anchor="middle" font-size="10" font-weight="500" fill="#2f3238">Paid vs. Denied</text>
    <circle cx="726" cy="686" r="98" fill="var(--ink)"/>
    <path d="M726,686 L726,588 A98 98 0 0 1 730.3,588.1 Z" fill="var(--orange)"/>
    <path d="M729,592 V565 H782" fill="none" stroke="#555" stroke-width=".7" stroke-dasharray="2 1.5"/>
    <text x="785" y="568" font-size="7" fill="#444">Denied : 0.7%</text>
    <path d="M683,795 H734 V782" fill="none" stroke="#555" stroke-width=".7" stroke-dasharray="2 1.5"/>
    <text x="635" y="798" font-size="7" fill="#444">Paid : 99.3%</text>
  </g>

  <!-- Paid vs Encounter -->
  <g class="chart-pie-encounter">
    <text x="720" y="872" text-anchor="middle" font-size="10" font-weight="500" fill="#2f3238">Paid vs. Encounter:</text>
    <circle cx="727" cy="1022" r="98" fill="var(--ink)"/>
    <path d="M727,1022 L633.2,993.7 A98 98 0 0 1 700,927.8 Z" fill="var(--orange)"/>
    <path d="M671,957 V905 H695" fill="none" stroke="#555" stroke-width=".7" stroke-dasharray="2 1.5"/>
    <text x="698" y="908" font-size="7" fill="#444">Paid : 15.9%</text>
    <path d="M680,1132 H736 V1118" fill="none" stroke="#555" stroke-width=".7" stroke-dasharray="2 1.5"/>
    <text x="614" y="1135" font-size="7" fill="#444">Encounter : 84.1%</text>
  </g>
</svg>

<footer class="footer">Copyright ©2016 ClaimScope. All Rights Reserved</footer>

</body>
</html>
```